International service dog training school needs web design

We need to upgrade our website. The website is https://brightpathmentor.site/
We help trainers and service dog programs learn how to train service dogs with the latest and most ethical training methods. We offer online and in-person coaching services. We would like to see designs that are engaging and communicate professionalism, expertise, and care for the dogs and people we work with. Please also keep the colors already in the logo in the design.

```html
<!DOCTYPE html>
<html lang="en">
<head>
<meta charset="utf-8">
<title>Bright Path Center for Assistance Dogs</title>
<link href="https://fonts.googleapis.com/css2?family=Jost:wght@400;500;600&family=Open+Sans:wght@400;600&display=swap" rel="stylesheet">
<style>
:root{
  --blue:#1b5dab;
  --blue-deep:#1a56a6;
  --teal:#17a091;
  --ink:#2f2f2f;
  --muted:#5a5a5a;
  --line:#e6e6e6;
  --white:#ffffff;
}
*{margin:0;padding:0;box-sizing:border-box}
html,body{width:1200px;height:4549px;overflow:hidden;background:var(--white)}
body{position:relative;font-family:"Jost",sans-serif;color:var(--ink)}
.abs{position:absolute}
.top-bar{left:0;top:0;width:1200px;height:5px;background:var(--blue)}
.header{left:0;top:5px;width:1200px;height:131px;background:var(--white);box-shadow:0 1px 4px rgba(0,0,0,.06);z-index:2}
.brand{left:111px;top:34px;display:flex;align-items:center;gap:12px}
.brand-dot{width:44px;height:44px;border-radius:50%;border:4px solid var(--teal);flex:none}
.brand-name{font-weight:500;color:var(--blue);font-size:19px;line-height:1.2;white-space:nowrap}
.nav{right:111px;top:56px;display:flex;gap:28px;font-size:15px;color:#444}
.nav a{color:inherit;text-decoration:none}
.nav a.active{color:var(--blue)}
.hero{left:0;top:136px;width:1200px;height:740px;background:linear-gradient(120deg,#8a6a4a 0%,#b48b5f 30%,#d9b58a 55%,#c7a27a 75%,#8d6c4e 100%)}
.hero-title{left:632px;top:412px;font-size:44px;font-weight:500;line-height:1.25;color:var(--white);text-shadow:0 2px 6px rgba(0,0,0,.25)}
.btn{display:inline-block;background:var(--blue);color:var(--white);font-size:16px;padding:0 22px;height:48px;line-height:48px;border-radius:3px;text-decoration:none}
.btn.grad{background:linear-gradient(90deg,var(--blue),var(--teal))}
.hero-btn{left:634px;top:548px;height:52px;line-height:52px;padding:0 24px}
.hero-wave{left:0;top:760px}
.about-title{left:111px;top:985px;font-size:40px;font-weight:500;color:var(--blue)}
.about-rule{left:111px;top:1046px;width:54px;height:2px;background:var(--blue)}
.about-text{left:111px;top:1078px;width:456px;font-family:"Open Sans",sans-serif;font-size:12.5px;line-height:30px;color:#333;text-align:justify}
.about-mark{left:680px;top:962px;width:406px;height:406px;border-radius:50%;border:14px solid var(--teal);display:flex;align-items:center;justify-content:center}
.about-mark span{font-size:30px;font-weight:500;color:var(--blue);text-align:center;line-height:1.3}
.divider{left:111px;top:1437px;width:978px;height:1px;background:var(--line)}
.photo{width:488px;height:365px;border-radius:3px}
.icon-ring{width:108px;height:108px;border-radius:50%;background:var(--white);border:3px solid var(--teal);display:flex;align-items:center;justify-content:center;box-shadow:0 0 0 6px rgba(255,255,255,.9)}
.svc-title{font-size:28px;font-weight:400;line-height:1.35;color:#222;width:360px}
.svc-text{font-size:15px;line-height:29px;color:var(--muted);width:360px;margin-top:18px}
.svc-block .btn{margin-top:28px}
.book-band{left:0;top:3657px;width:1200px;height:560px;background:var(--teal)}
.book-title{left:175px;top:3823px;font-size:30px;font-weight:500;color:var(--white)}
.book-sub{left:175px;top:3876px;width:520px;font-size:22px;line-height:38px;color:var(--white)}
.book-btn{left:175px;top:3969px;height:50px;line-height:50px}
.book-cover{left:759px;top:3700px;width:232px;height:412px;background:linear-gradient(160deg,#f4f1ec,#d9cfc2 60%,#b8443e 100%);box-shadow:6px 6px 14px rgba(0,0,0,.25);border-right:10px solid #b3262c}
.footer{left:0;top:4120px;width:1200px;height:429px}
.foot-brand{left:0;top:4236px;width:1200px;display:flex;justify-content:center;align-items:center;gap:14px}
.foot-brand .brand-dot{border-color:var(--white);width:52px;height:52px}
.foot-brand .brand-name{color:var(--white);font-size:30px}
.foot-nav{left:0;top:4370px;width:1200px;display:flex;justify-content:center;gap:33px;font-size:17px;color:var(--white)}
.socials{left:0;top:4426px;width:1200px;display:flex;justify-content:center;gap:8px}
.socials span{width:36px;height:36px;border-radius:50%;border:2px solid var(--white)}
.copyright{left:0;top:4489px;width:1200px;text-align:center;font-size:14px;color:var(--white)}
.version{left:1088px;top:4524px;font-size:14px;color:#cfe0f3}
</style>
</head>
<body>
<div class="abs top-bar"></div>
<header class="abs header">
  <div class="abs brand"><span class="brand-dot"></span><span class="brand-name">Marion Delacroix Ph.D.<br>Bright Path Center</span></div>
  <nav class="abs nav"><a class="active" href="#">Home</a><a href="#">The Center</a><a href="#">Helping organizations</a><a href="#">Teaching Trainers</a><a href="#">Research</a><a href="#">Contact</a></nav>
</header>

<section class="abs hero" role="img" aria-label="Photo of a brown pointer dog standing in a golden grass field at sunset"></section>
<svg class="abs hero-wave" width="1200" height="140" viewBox="0 0 1200 140">
  <path d="M0 20 Q560 180 1200 0 L1200 140 L0 140 Z" fill="#ffffff"/>
  <path d="M0 14 Q560 172 1200 -4 L1200 8 Q560 182 0 30 Z" fill="#1b5dab"/>
  <path d="M0 4 Q420 140 900 70 Q520 150 0 22 Z" fill="#17a091"/>
</svg>
<h1 class="abs hero-title">Coaching for Services<br>Dog Professionals</h1>
<a class="abs btn hero-btn" href="#">Read More</a>

<h2 class="abs about-title">ABOUT US</h2>
<div class="abs about-rule"></div>
<p class="abs about-text">The Bright Path Center for Assistance Dogs was founded by Marion Delacroix Ph.D. in response to demand for coaching from dog trainers, medical professionals, and service dog programs. Marion Delacroix Ph.D. has helped hundreds of trainers and several programs both in the US and internationally, expand the type of dogs they could offer to include medical alert dogs. Specialized mostly in the training of diabetic alert dogs, seizure dogs, and psychiatric service dogs, Marion Delacroix is also experienced in the training of mobility assistance dogs and autism dogs. The coaching is individually catered to meet the programs' needs.</p>
<div class="abs about-mark"><span>Bright Path<br>Center</span></div>
<div class="abs divider"></div>

<div class="abs photo" style="left:111px;top:1495px;background:linear-gradient(180deg,#cfcac2,#6a7a8e 50%,#b9b2a6)" role="img" aria-label="Group photo of trainers in blue shirts with a dog"></div>
<div class="abs icon-ring" style="left:542px;top:1624px"><svg width="56" height="56" viewBox="0 0 56 56" fill="none" stroke="#1b5dab" stroke-width="2"><circle cx="28" cy="10" r="5"/><rect x="21" y="17" width="14" height="7"/><path d="M28 24v8M12 32h32M12 32v6M28 32v6M44 32v6"/><circle cx="12" cy="42" r="4"/><circle cx="28" cy="42" r="4"/><circle cx="44" cy="42" r="4"/></svg></div>
<div class="abs svc-block" style="left:699px;top:1550px"><h3 class="svc-title">Organization/Program Consulting</h3><p class="svc-text">Helping organizations get started, improve their training program, and add services</p><a class="btn grad" href="#">Learn More</a></div>

<div class="abs photo" style="left:600px;top:1920px;background:linear-gradient(180deg,#e7e5e1,#8a7462 55%,#4a4a4a)" role="img" aria-label="Trainer working with a black dog indoors"></div>
<div class="abs icon-ring" style="left:542px;top:2049px"><svg width="56" height="56" viewBox="0 0 56 56" fill="none" stroke="#1b5dab" stroke-width="2"><circle cx="40" cy="12" r="5"/><path d="M40 18v20M34 26h12M36 48l4-10 4 10"/><path d="M8 34q4-10 14-8l4 6-4 4v10M12 36v10"/></svg></div>
<div class="abs svc-block" style="left:150px;top:1983px"><h3 class="svc-title">Professional coaching teaching for dog trainers</h3><p class="svc-text">Helping dog trainers improve their skills and learn about service dog training and medical alert dog training.</p><a class="btn grad" href="#">Learn More</a></div>

<div class="abs photo" style="left:111px;top:2346px;background:linear-gradient(180deg,#bdb6ad,#d6cdbf 60%,#a89d90)" role="img" aria-label="Detection dog sniffing paint cans on a tiled floor"></div>
<div class="abs icon-ring" style="left:542px;top:2475px"><svg width="56" height="56" viewBox="0 0 56 56" fill="none" stroke="#1b5dab" stroke-width="2"><path d="M8 28h40l-4 16H12z"/><path d="M12 28q16-14 32 0"/><circle cx="28" cy="37" r="3"/></svg></div>
<div class="abs svc-block" style="left:699px;top:2400px"><h3 class="svc-title">Collaborating in Research Projects</h3><p class="svc-text">Collaborating in research studies in the field of Medical Detection Dogs.</p><a class="btn grad" href="#">Learn More</a></div>

<div class="abs photo" style="left:600px;top:2771px;background:linear-gradient(180deg,#4a4a58,#8f8a86 50%,#3e3a38)" role="img" aria-label="Audience seated in a lecture hall facing a projection screen"></div>
<div class="abs icon-ring" style="left:542px;top:2900px"><svg width="56" height="56" viewBox="0 0 56 56" fill="none" stroke="#1b5dab" stroke-width="2"><rect x="10" y="8" width="36" height="22"/><path d="M16 24l8-8 6 5 10-9"/><circle cx="16" cy="40" r="4"/><circle cx="28" cy="40" r="4"/><circle cx="40" cy="40" r="4"/></svg></div>
<div class="abs svc-block" style="left:150px;top:2868px"><h3 class="svc-title">Presentations and Seminars</h3><p class="svc-text">Sharing knowledge about service dogs and medical detection.</p><a class="btn grad" href="#">Learn More</a></div>

<div class="abs photo" style="left:111px;top:3196px;background:linear-gradient(180deg,#e8ebee,#b9c0c6 55%,#5a4640)" role="img" aria-label="Service dog in a red vest looking out an airport window"></div>
<div class="abs icon-ring" style="left:542px;top:3325px"><svg width="56" height="56" viewBox="0 0 56 56" fill="none" stroke="#1b5dab" stroke-width="2"><circle cx="28" cy="28" r="18"/><ellipse cx="28" cy="28" rx="8" ry="18"/><path d="M10 28h36M13 19h30M13 37h30"/></svg></div>
<div class="abs svc-block" style="left:699px;top:3278px"><h3 class="svc-title">International services</h3><p class="svc-text">Fluent in both English and French, in-person and online coaching around the world.</p><a class="btn grad" href="#">Learn More</a></div>

<section class="abs book-band"></section>
<h2 class="abs book-title">New book from Marion Delacroix Ph.D!</h2>
<p class="abs book-sub">Choosing and Guiding your Assistance Dog: Steps to confident public outings</p>
<a class="abs btn book-btn" href="#">Read More</a>
<div class="abs book-cover" role="img" aria-label="Book cover with a service dog in a red vest"></div>

<svg class="abs footer" width="1200" height="429" viewBox="0 0 1200 429">
  <path d="M0 0 Q600 150 1200 0 L1200 429 L0 429 Z" fill="#1a56a6"/>
</svg>
<div class="abs foot-brand"><span class="brand-dot"></span><span class="brand-name">Marion Delacroix Ph.D.</span></div>
<nav class="abs foot-nav"><span>Home</span><span>The Center</span><span>Helping organizations</span><span>Teaching Trainers</span><span>Research</span><span>Contact</span></nav>
<div class="abs socials"><span></span><span></span><span></span><span></span><span></span></div>
<p class="abs copyright">©2021 Company Name.All rights reserved.</p>
<span class="abs version">C2</span>
</body>
</html>
```